Veltrix Stationary

Design the stationary of Veltrix Promotions Group.

Veltrix is a BTL company, BTL meaning "below the line". In other words Veltrix is a Promotional Marketing company (the company that design the brands promotional activities).

The design should transmit creativity, agility, boldness.

I need:
* Bis Card
* Letter head
* Envelopes, both vertical and horizontal (for legal size), and letter envelope
* Folders
* PPT template (Title page and regular page)
* CD slip (CD envelope)
* ID card (employee card)

And what ever else you want to throw in.
Updates

Guys,

Something I missed from the brief.   The predominat color should be RED.

Also, have fun and play with the exclamation mark (!) of the logo. 

Hi guys, more comments:

Remember that Veltrix is a "creativity" agency, not in the advertising side but on the promotional side, and that should reflect on the stationary.

 I want a bold design.  Bold and yet crisp.

 

Guys, i just uploaded the Logo in AI format.

I Also uploaded the actual Veltrix Bis Card, wich I like.  So I will like to see some designs with that bis card approach.

Guys, I am so sorry, but I notice in your last post that I upladed a wrong design ("13154_marketing_group_veltrix_brief225630.ai").  The problem was that I asked the designer the file in AI format and he send me thw wrong file, and since I dont have Illustrator I could not verify it.

The differences are minor, I just already ask him the correct one (similar to the EPS file).

Sorry                                   

Just post the correct AI file : "Veltrix Logo.ai"

Reason: I'm expecting more designs to choose from and also I wont be available tomorrow to decide.

Reason: Sorry guys, but we are not there yet!

Target Market(s)

Marketing directors, Marketing Managers

Industry/Entity Type

Legal

Requirements
Must have
• Must work with the logo attached.
The predominat color should be RED.
Play and have fun with the exclamation mark (!).
Should not have
• * No old fonts

Should not be:
* boring
* Informal
* rigid

```html
<!DOCTYPE html>
<html lang="en">
<head>
<meta charset="utf-8">
<title>Veltrix Promotions Group – Stationery</title>
<link href="https://fonts.googleapis.com/css2?family=Open+Sans:wght@400;600;800&display=swap" rel="stylesheet">
<style>
  :root {
    --backdrop: #2a2a2b;
    --paper: #ffffff;
    --brand-red: #c8101a;
    --brand-red-dark: #a80c14;
    --ink: #1c1c1c;
    --ink-soft: #333333;
    --band-grey: #8a8a8a;
    --sleeve-band: #e9e5e5;
    --disc-rim: #b9b9bd;
    --disc-hub: #d8d8dc;
  }
  * { box-sizing: border-box; margin: 0; padding: 0; }
  html, body { width: 900px; height: 1200px; overflow: hidden; background: var(--backdrop); }
  body { font-family: "Open Sans", Arial, sans-serif; color: var(--ink); }
  .canvas { position: relative; width: 900px; height: 1200px; background: var(--backdrop); }

  .brand-name { font-weight: 800; letter-spacing: -0.5px; line-height: 1; display: flex; align-items: center; gap: 6px; }
  .brand-dot { width: 10px; height: 10px; border-radius: 50%; background: var(--brand-red); display: inline-block; }

  /* Window envelope, front */
  .envelope-front { position: absolute; left: 32px; top: 55px; width: 695px; height: 310px; background: var(--paper); box-shadow: 0 4px 14px rgba(0,0,0,.5); }
  .envelope-front .brand-name { position: absolute; left: 26px; top: 28px; font-size: 36px; color: var(--ink); }
  .address-window { position: absolute; left: 26px; top: 131px; width: 230px; height: 88px; border-radius: 14px; background: #fff; box-shadow: inset 0 0 0 1px #d6d6d6, 0 2px 6px rgba(0,0,0,.35); }
  .sender { position: absolute; left: 30px; top: 255px; font-size: 8.5px; line-height: 11px; color: var(--ink-soft); }
  .sender .sender-name { font-size: 10px; font-weight: 600; color: var(--ink); }
  .sender-contact { position: absolute; left: 144px; top: 267px; padding-left: 12px; border-left: 1px solid #777; font-size: 8.5px; line-height: 11px; color: var(--ink-soft); }
  .sender-contact b { color: var(--brand-red); font-weight: 600; }
  .footer-band { position: absolute; left: 0; bottom: 0; width: 100%; height: 14px; background: var(--band-grey); }
  .corner-mark { position: absolute; right: 20px; bottom: 8px; width: 120px; height: 80px; background: linear-gradient(135deg, var(--brand-red), var(--brand-red-dark)); border-radius: 4px; }

  /* Envelope, back with flap */
  .envelope-back { position: absolute; left: 143px; top: 423px; width: 694px; height: 305px; background: var(--paper); box-shadow: 0 4px 14px rgba(0,0,0,.5); }
  .envelope-back svg { position: absolute; left: 0; top: 0; }

  /* CD sleeve */
  .cd-sleeve { position: absolute; left: 32px; top: 768px; width: 370px; height: 352px; background: var(--brand-red); box-shadow: 0 4px 14px rgba(0,0,0,.5); overflow: hidden; }
  .cd-sleeve .pattern-field { position: absolute; inset: 0; background: linear-gradient(180deg, var(--brand-red), var(--brand-red-dark)); }
  .sleeve-title { position: absolute; right: 20px; top: 20px; text-align: right; color: #fff; }
  .sleeve-title .headline { font-size: 20px; font-weight: 400; line-height: 24px; }
  .sleeve-title .subline { font-size: 11.5px; line-height: 14px; }
  .sleeve-band { position: absolute; left: 0; top: 122px; width: 100%; height: 108px; background: var(--sleeve-band); }
  .sleeve-band .brand-name { position: absolute; left: 14px; top: 36px; font-size: 36px; color: var(--ink); }
  .thumb-notch { position: absolute; left: 316px; top: 118px; width: 116px; height: 116px; border-radius: 50%; background: var(--backdrop); }

  /* Discs */
  .disc-stack { position: absolute; left: 420px; top: 780px; }
  .disc-label { font-family: "Open Sans", Arial, sans-serif; font-size: 7.5px; fill: #fff; }
  .disc-brand { font-family: "Open Sans", Arial, sans-serif; font-size: 28px; font-weight: 800; fill: #fff; }
</style>
</head>
<body>
<main class="canvas">

  <section class="envelope-front" aria-label="Window envelope">
    <div class="brand-name">veltrix <span class="brand-dot"></span></div>
    <div class="address-window"></div>
    <div class="sender">
      <div class="sender-name">Veltrix Promotions Group</div>
      <div>Street, Region, Country</div>
      <div>PO BOX 321</div>
    </div>
    <div class="sender-contact">
      <div><b>P</b> +31 (6) 20 48 11 35</div>
      <div><b>F</b> +31 (6) 20 48 11 36</div>
    </div>
    <div class="footer-band"></div>
    <div class="corner-mark" role="img" aria-label="Red brand emblem decoration in the corner"></div>
  </section>

  <section class="envelope-back" aria-label="Envelope back with flap">
    <svg width="694" height="305" viewBox="0 0 694 305">
      <path role="img" aria-label="Red flap with repeating brand pattern"
        d="M0 0 H694 V82 Q694 104 672 104 C560 96 420 94 330 96 C230 98 120 92 36 102 Q0 106 0 82 Z"
        fill="#c8101a"/>
    </svg>
  </section>

  <section class="cd-sleeve" aria-label="CD sleeve">
    <div class="pattern-field" role="img" aria-label="Red repeating brand pattern"></div>
    <div class="sleeve-title">
      <div class="headline">Lorem ispum text</div>
      <div class="subline">Place your text</div>
    </div>
    <div class="sleeve-band">
      <div class="brand-name">veltrix <span class="brand-dot"></span></div>
    </div>
    <div class="thumb-notch"></div>
  </section>

  <svg class="disc-stack" width="460" height="330" viewBox="0 0 460 330" aria-label="CD discs">
    <defs>
      <path id="ring-1" d="M35 165 a130 130 0 1 1 260 0 a130 130 0 1 1 -260 0"/>
      <path id="ring-2" d="M55 165 a130 130 0 1 1 260 0 a130 130 0 1 1 -260 0"/>
      <path id="ring-3" d="M95 165 a130 130 0 1 1 260 0 a130 130 0 1 1 -260 0"/>
      <path id="ring-4" d="M165 165 a130 130 0 1 1 260 0 a130 130 0 1 1 -260 0"/>
    </defs>
    <g class="disc">
      <circle cx="165" cy="165" r="150" fill="#b9b9bd"/>
      <circle cx="165" cy="165" r="145" fill="#c8101a"/>
      <text class="disc-label"><textPath href="#ring-1">00. Address Line 1 | Address Line 2 | Phone: 000 XXX 0000 | Fax: 000 XXX 0000 | info@veltrixpromo.example</textPath></text>
    </g>
    <g class="disc">
      <circle cx="185" cy="165" r="150" fill="#b9b9bd"/>
      <circle cx="185" cy="165" r="145" fill="#c8101a"/>
      <text class="disc-label"><textPath href="#ring-2">00. Address Line 1 | Address Line 2 | Phone: 000 XXX 0000 | Fax: 000 XXX 0000 | info@veltrixpromo.example</textPath></text>
    </g>
    <g class="disc">
      <circle cx="225" cy="165" r="150" fill="#b9b9bd"/>
      <circle cx="225" cy="165" r="145" fill="#c8101a"/>
      <text class="disc-label"><textPath href="#ring-3">00. Address Line 1 | Address Line 2 | Phone: 000 XXX 0000 | Fax: 000 XXX 0000 | info@veltrixpromo.example</textPath></text>
    </g>
    <g class="disc">
      <circle cx="295" cy="165" r="150" fill="#b9b9bd"/>
      <circle cx="295" cy="165" r="145" fill="#c8101a"/>
      <text class="disc-label"><textPath href="#ring-4">00. Address Line 1 | Address Line 2 | Phone: 000 XXX 0000 | Fax: 000 XXX 0000 | info@veltrixpromo.example | www.veltrixpromo.example</textPath></text>
      <circle cx="295" cy="165" r="48" fill="#d8d8dc"/>
      <circle cx="295" cy="165" r="34" fill="#c4c4c8"/>
      <circle cx="295" cy="165" r="18" fill="#2a2a2b"/>
      <text class="disc-brand" x="243" y="255">veltrix</text>
      <circle cx="352" cy="245" r="6" fill="#fff"/>
    </g>
  </svg>

</main>
</body>
</html>
```